Best in class business looking for best in class stationery that accurately reflects the brand image we are trying to build as the brand expands throughout the country. The Varying items should be an eye catching design that makes even the simplest letter or small business card stand out in the crowd.

Target Market(s)

Professionals

Industry/Entity Type

Real Estate

Other font styles liked:
• See atttached logo

Requirements
Must have
• Letterhead
• Business cards
• Envelopes
• Labels for larger mailings
Nice to have
• Folders
• Notebook
Should not have
• Stale design elements

```html
<!DOCTYPE html>
<html lang="en">
<head>
<meta charset="utf-8">
<title>Ridgeline Property Group – Letterhead and Cover</title>
<link rel="stylesheet" href="https://fonts.googleapis.com/css2?family=Arimo:wght@400;700&family=Oswald:wght@600&display=swap">
<style>
  :root {
    --backdrop: #d4d4d4;
    --brand-blue: #3d4fa0;
    --cover-grey: #9b9b9b;
    --cover-grey-dark: #8f8f8f;
    --paper: #fbfbfb;
    --body-text: #5a5a5a;
    --meta-text: #6a6a6a;
    --watermark: #d9dbe3;
  }
  * { margin: 0; padding: 0; box-sizing: border-box; }
  html, body { width: 1200px; height: 800px; overflow: hidden; }
  body {
    position: relative;
    background: var(--backdrop);
    font-family: "Arimo", Arial, sans-serif;
  }
  .sheet-title {
    position: absolute;
    top: 36px;
    font-family: "Oswald", "Arial Narrow", sans-serif;
    font-weight: 600;
    font-size: 17px;
    color: var(--brand-blue);
    letter-spacing: 0.3px;
    text-align: center;
  }
  .sheet-title--cover { left: 90px; width: 455px; }
  .sheet-title--letter { left: 665px; width: 460px; }

  /* Shared brand name */
  .brand {
    display: flex; align-items: center; justify-content: center; gap: 6px;
    color: var(--brand-blue);
    font-weight: 700;
    text-transform: uppercase;
    white-space: nowrap;
  }
  .brand__mark { background: var(--brand-blue); flex: none; }

  /* Cover */
  .cover {
    position: absolute;
    left: 90px; top: 82px;
    width: 455px; height: 646px;
    overflow: hidden;
    background: linear-gradient(160deg, var(--cover-grey), var(--cover-grey-dark));
  }
  .cover__tab {
    position: absolute;
    left: 451px; top: 212px;
    width: 4px; height: 164px;
    background: var(--brand-blue);
  }
  .cover__brand {
    position: absolute;
    left: 222px; top: 316px;
    width: 220px;
    font-size: 11px; letter-spacing: 0.3px;
  }
  .cover__brand .brand__mark { width: 10px; height: 10px; }
  .cover__url {
    position: absolute;
    left: 0; right: 0; top: 626px;
    text-align: center;
    font-size: 8px; font-weight: 700;
    color: var(--brand-blue);
    letter-spacing: 0.3px;
  }

  /* Letterhead */
  .letter {
    position: absolute;
    left: 665px; top: 82px;
    width: 460px; height: 646px;
    overflow: hidden;
    background: var(--paper);
  }
  .letter__brand {
    position: absolute;
    left: 14px; top: 60px;
    font-size: 8.5px; letter-spacing: 0.3px;
    justify-content: flex-start;
  }
  .letter__brand .brand__mark { width: 8px; height: 8px; }
  .letter__rule {
    position: absolute;
    left: 0; top: 110px;
    width: 6px; height: 75px;
    background: var(--brand-blue);
  }
  .meta {
    position: absolute;
    left: 4px; top: 112px;
    width: 61px;
    text-align: right;
    font-size: 6px;
    line-height: 8.5px;
    color: var(--meta-text);
    white-space: nowrap;
  }
  .meta dt { font-weight: 700; color: var(--brand-blue); }
  .meta dd { margin-bottom: 5px; }
  .recipient {
    position: absolute;
    left: 74px; top: 113px;
    font-size: 8px; line-height: 9.5px;
    color: var(--body-text);
  }
  .letter__body {
    position: absolute;
    left: 74px; top: 174px;
    width: 312px;
    font-size: 7.6px; line-height: 9.6px;
    color: var(--body-text);
    text-align: justify;
  }
  .letter__body p { margin-bottom: 9.6px; }
  .letter__salutation { font-size: 6.5px; }
  .signoff {
    position: absolute;
    left: 74px; top: 456px;
    font-size: 7.6px; line-height: 9.6px;
    color: var(--body-text);
  }
  .signoff p { margin-bottom: 8px; }
  .signature {
    position: absolute;
    left: 74px; top: 488px;
    width: 96px; height: 28px;
    background: linear-gradient(90deg, #e6e6e6, #f1f1f1);
  }
  .contact {
    position: absolute;
    left: 18px; top: 578px;
    font-size: 4.8px; line-height: 7px;
    font-style: normal;
    color: var(--meta-text);
  }
  .contact__name { font-weight: 700; color: var(--brand-blue); font-size: 5.5px; margin-bottom: 4px; }
  .contact__row { display: flex; align-items: flex-start; gap: 4px; }
  .contact__row svg { flex: none; margin-top: 1px; }
  .contact__row + .contact__row { margin-top: 1px; }
  .contact__row--spaced { margin-top: 4px !important; }
  .letter__watermark {
    position: absolute;
    left: 232px; top: 604px;
    width: 220px;
    font-size: 10.5px; letter-spacing: 0.3px;
    color: var(--watermark);
  }
  .letter__watermark .brand__mark { width: 10px; height: 10px; background: var(--watermark); }
</style>
</head>
<body>

  <h2 class="sheet-title sheet-title--cover">LETTERHEAD COVER</h2>
  <h2 class="sheet-title sheet-title--letter">LETTERHEAD</h2>

  <section class="cover" aria-label="Letterhead cover">
    <div class="brand cover__brand"><span class="brand__mark"></span>Ridgeline Property Group</div>
    <div class="cover__tab"></div>
    <div class="cover__url">WWW.RIDGELINEPG.COM</div>
  </section>

  <section class="letter" aria-label="Letterhead">
    <div class="brand letter__brand"><span class="brand__mark"></span>Ridgeline Property Group</div>

    <div class="letter__rule"></div>
    <dl class="meta">
      <dt>To</dt><dd>Mauris Euismod</dd>
      <dt>Subject</dt><dd>Egestas Ornare</dd>
      <dt>Date</dt><dd>10,18,2016</dd>
    </dl>

    <div class="recipient">
      To the General Director,<br>
      Holloway Trade Incorporated.<br>
      20 / 07 /2014
    </div>

    <div class="letter__body">
      <p class="letter__salutation">Dear Sir / Madam</p>
      <p>Lorem ipsum dolor sit amet, consectetuer adipiscing elit. Nam cursus. Morbi ut mi. Li balam enim leo, egestas id, condimentum at, laoreet mattis, massa. Sed eleifend nos ummy diam. Praesent mauris ante, elementum et, bibendum at, posuere sit amet, nib duis tincidunt lectus quis dui viverra vestibulum. Suspendisse vulputate aliquam dui. Nulla elementum dui ut augue. Aliquam vehicula mi at mauris. Maecenas placerat sea si at consequat rhoncus, sem nunc gravida justo.</p>
      <p>Sed laoreet aliquamlii amet, consectetuer adipiscing elit. Nam cursus. Morbi ut mi. Lie balam enim leo, egestas id, condimentum at, laoreet mattis, massa. Sed eleifend nos ummy diam. Praesent mauris ante, elementum et, bibendum at.</p>
      <p>Nulla elementum dui ut augue. consectetuer adipiscing elit. Nam cursus. Morbi ut ma balam enim leo, egestas id, condimentum at, laoreet mattis, massa. Sed eleifend nos ummy diam. Praesent mauris ante, elementum et, bibendum at, posuere sit amet, nib duis tincidunt lectus quis dui viverra vestibulum. Suspendisse vulputate aliquam duifi. Nulla elementum dui ut augue. Aliquam vehicula mi at mauris. Maecenas placerat sef si at consequat rhoncus, sem nunc gravida justo.Fusce suscipit varius mi. Cum sociisz tes, nascetur ridiculus mus. Nulla dui. Morbi nunc odio, gravida at, cursus nec, luctusi lorem.Maecenas tristique orci ac sem. amin deso as. Duis ultricies pharetra agna. Dai nec accumsan malesuada orci. Donec</p>
      <p>liquam vehicula mi at mauris. Maecenas placerat se si at consequat rhoncus, sem nim gravida justo.Fusce suscipit varius mi. Cum sociis tes, nascetur ridiculus mus. Nulla al Morbi nunc odio, gravida at, cursus nec, luctusi. lorem.Maecenas tristique orci ac seai amin deso as.</p>
    </div>

    <div class="signoff">
      <p>Sincerely,</p>
      <p>Adrian Kessler.</p>
    </div>
    <div class="signature" role="img" aria-label="Handwritten signature of Adrian Kessler"></div>

    <address class="contact">
      <div class="contact__name">RIDGELINE PROPERTY</div>
      <div class="contact__row">
        <svg width="5" height="6" viewBox="0 0 10 12" aria-hidden="true"><path d="M5 0a4 4 0 0 0-4 4c0 3 4 8 4 8s4-5 4-8a4 4 0 0 0-4-4z" fill="var(--brand-blue)"/><circle cx="5" cy="4" r="1.5" fill="#fff"/></svg>
        <span>14 Birchwood Ave<br>Ashford, MA 01000</span>
      </div>
      <div class="contact__row contact__row--spaced">
        <svg width="5" height="6" viewBox="0 0 10 12" aria-hidden="true"><rect x="2" y="0" width="6" height="12" rx="1.5" fill="var(--brand-blue)"/></svg>
        <span>(413) 555-0142</span>
      </div>
      <div class="contact__row">
        <svg width="5" height="6" viewBox="0 0 12 12" aria-hidden="true"><circle cx="6" cy="6" r="5" fill="none" stroke="var(--brand-blue)" stroke-width="1.6"/><path d="M1 6h10M6 1c-3 3-3 7 0 10M6 1c3 3 3 7 0 10" fill="none" stroke="var(--brand-blue)" stroke-width="1"/></svg>
        <span>www.ridgelinepg.com</span>
      </div>
      <div class="contact__row">
        <svg width="5" height="6" viewBox="0 0 12 10" aria-hidden="true"><rect x="0" y="1" width="12" height="8" fill="var(--brand-blue)"/><path d="M0 1l6 5 6-5" fill="none" stroke="#fff" stroke-width="1"/></svg>
        <span>leasing@ridgelinepg.com</span>
      </div>
    </address>

    <div class="brand letter__watermark"><span class="brand__mark"></span>Ridgeline Property Group</div>
  </section>

</body>
</html>
```